ZEPRILO.COM is a premium domain sales company. Our competitors are companies like vastplots.example, getparcels.example, peerwords.example. Our current site is at www.zeprilos.example.

We want to have the ability to search for domains, to highlight special offers and have some testimonials on the index page.

The logo for the site is attached.

Please be sure that the order form fits on the screen without scrolling the page. I want the entire form, including the submit button to fit without any page scrolling.

Delivered product - INDEX PAGE, ORDER FORM AND CONTENT PAGE PSDs.

Target Market(s)

Small to Medium business professionals

Industry/Entity Type

It Company

Requirements
Must have
• 1. List of domains for sale
2. Simple search box with button to run the search
3. link for advanced search
4. testimonial area. Note - this can be a small box where a different testimonial is displayed on each page load.
Nice to have
• Would like the site to have some white space. Don't want a heavily packed website. Give it an "airy" feel.

```html
<!DOCTYPE html>
<html lang="en">
<head>
<meta charset="utf-8">
<title>ZEPRILO.COM – Order Form</title>
<link rel="stylesheet" href="https://fonts.googleapis.com/css2?family=PT+Sans:ital,wght@0,400;0,700;1,400&family=Roboto+Condensed:wght@400;700&family=Arimo:wght@400;700&display=swap">
<style>
:root{
  --ink:#1a1a1a;
  --muted:#6b6b6b;
  --green:#4a9a1e;
  --green-dark:#2f7d14;
  --green-band:#3d8a22;
  --blue:#0b55a0;
  --link:#1a8fd6;
  --nav:#1b1b1b;
  --field-bg:#f2f3f1;
  --card-bg:#e4e5e2;
  --line:#d6d6d6;
  --footer:#1c1c1c;
  --footer-text:#8a8a8a;
  --teal-top:#ffffff;
  --teal-bottom:#a9d5c3;
}
*{box-sizing:border-box;margin:0;padding:0}
html,body{width:1200px;height:705px;overflow:hidden}
body{position:relative;background:#fff;font-family:"Arimo",Arial,sans-serif;color:var(--ink)}
.backdrop{position:absolute;left:0;top:0;width:1200px;height:449px;background:linear-gradient(var(--teal-top),var(--teal-bottom))}
.sheet{position:absolute;left:161px;top:0;width:878px;height:606px;background:#fff}
.abs{position:absolute}
.brand{left:191px;top:20px;font:700 30px "Arimo",Arial,sans-serif;color:var(--green-dark);letter-spacing:-0.5px}
.phone{left:865px;top:34px;display:flex;align-items:center;gap:8px;font-size:15px;color:var(--green-dark)}
.nav{left:180px;top:77px;width:835px;height:41px;background:var(--nav);display:flex;font:400 11px "Roboto Condensed",Arial,sans-serif;color:#fff;text-transform:uppercase}
.nav a{color:#fff;text-decoration:none;line-height:41px}
.nav .home{background:var(--blue);width:73px;text-align:center}
.nav .item{position:absolute;top:0}
.help{right:0;top:0;width:151px;height:41px;background:linear-gradient(#6fbd3d,#46951f);display:flex;align-items:center;gap:10px;padding-left:14px;text-transform:none}
.help strong{display:block;font:700 12px "Arimo",Arial,sans-serif;color:#111}
.help span{display:block;font:700 9px "Arimo",Arial,sans-serif;color:#fff}
.notice{left:180px;top:134px;width:550px;height:69px;background:#f5f5f5;border:1px solid var(--line);border-radius:3px}
.notice h1{position:absolute;left:79px;top:12px;font:400 19px "Arimo",Arial,sans-serif;color:var(--green)}
.notice p{position:absolute;left:81px;top:38px;font-size:13px}
.notice p a{color:var(--blue);text-decoration:none}
.notice .price{position:absolute;right:13px;top:30px;font-size:17px}
.summary{left:757px;top:134px;width:259px;height:136px;background:#f3f3f3;border:1px solid var(--line);border-radius:4px;overflow:hidden}
.summary h2{height:31px;background:var(--nav);color:#fff;font:400 13px "Arimo",Arial,sans-serif;line-height:31px;padding-left:10px}
.summary .lbl{position:absolute;font-size:13px;color:#8d8d8d}
.summary .total{position:absolute;left:19px;top:95px;font:700 26px "Arimo",Arial,sans-serif;color:var(--green)}
.apply{position:absolute;left:207px;top:46px;font:700 11px "Arimo",Arial,sans-serif;color:var(--link);text-decoration:underline}
.field{position:absolute;height:26px;background:#fff;border:1px solid #dcdcdc;border-radius:3px;box-shadow:inset 0 1px 2px rgba(0,0,0,.06)}
.methods{left:184px;top:217px;font:700 16px "Arimo",Arial,sans-serif}
.tab{position:absolute;top:246px;height:39px;font:400 16px "Arimo",Arial,sans-serif;display:flex;align-items:center;justify-content:center}
.tab.card{left:180px;width:106px;background:var(--green-band);color:#fff;border-radius:3px 3px 0 0}
.tab.alt{left:288px;width:79px;background:linear-gradient(#fff,#e3e3e3);border:1px solid #ccc;border-bottom:none;color:#333;font-size:15px}
.tab.invoice{left:370px;width:97px;background:#cfcfcf;color:#333}
.band{left:180px;top:285px;width:836px;height:40px;background:var(--green-band);border-top:4px solid #57a530;font:italic 400 14px "PT Sans",sans-serif;color:#cfe9b4}
.band span{position:absolute;top:10px}
.billing{left:180px;top:325px;width:550px;height:251px;background:var(--field-bg)}
.cardinfo{left:730px;top:325px;width:286px;height:251px;background:var(--card-bg)}
.label{position:absolute;font:400 13px "PT Sans",sans-serif;color:#555}
.select{position:absolute;height:26px;background:#fff;border:1px solid #dcdcdc;border-radius:3px;font:400 10px "PT Sans",sans-serif;color:#999;line-height:24px;padding-left:7px}
.select.dark{color:#222}
.select i{position:absolute;right:0;top:-1px;width:28px;height:26px;background:#222;border-radius:0 3px 3px 0}
.select i::after{content:"";position:absolute;left:9px;top:10px;border:5px solid transparent;border-top:6px solid #fff}
.terms{left:762px;top:487px;width:225px;font-size:10px;line-height:12px;color:#333}
.terms a{color:var(--link);font-weight:700}
.checkout{left:869px;top:523px;width:132px;height:39px;background:linear-gradient(#5cb82a,#3e9515);border:1px solid #3b8a15;border-radius:3px;display:flex;align-items:center;justify-content:center;gap:7px;color:#fff;font:700 11px "Roboto Condensed",Arial,sans-serif}
.footer{left:0;top:606px;width:1200px;height:99px;background:var(--footer);border-top:4px solid #1e7a4a}
.flinks{left:172px;top:17px;font:400 10px "PT Sans",sans-serif;color:var(--footer-text)}
.copy{left:172px;top:36px;font:400 10px "PT Sans",sans-serif;color:var(--footer-text)}
.social{position:absolute;top:64px;width:20px;height:20px;border-radius:50%;background:#7d7d7d}
.badge{left:623px;top:25px;width:193px;height:56px;background:#1a5fa8;display:flex;align-items:center;gap:12px;padding-left:12px;color:#fff}
.badge b{font:700 30px "Arimo",Arial,sans-serif}
.badge span{font:700 11px "Arimo",Arial,sans-serif;line-height:14px}
.fbrand{left:920px;top:38px;font:700 20px "Arimo",Arial,sans-serif;color:#4a4a4a}
</style>
</head>
<body>
<div class="backdrop"></div>
<div class="sheet"></div>

<header>
  <div class="abs brand">ZEPRILO.COM</div>
  <div class="abs phone">
    <svg width="16" height="14" viewBox="0 0 16 14"><path d="M1 5c0-3 14-3 14 0l-1 2-3-1V4H5v2L2 7z" fill="#111"/><rect x="3" y="8" width="10" height="5" rx="1" fill="#111"/><circle cx="8" cy="10.5" r="1.6" fill="#fff"/></svg>
    <span>+1 555.010.4827</span>
  </div>
  <nav class="abs nav">
    <a class="home" href="#">Home</a>
    <a class="item" style="left:91px" href="#">About Us</a>
    <a class="item" style="left:180px" href="#">FAQ</a>
    <a class="item" style="left:239px" href="#">Testimonials</a>
    <a class="item" style="left:347px" href="#">Support</a>
    <a class="item" style="left:431px" href="#">Contact</a>
    <div class="abs help">
      <svg width="18" height="16" viewBox="0 0 18 16"><path d="M1 1h16v10H7l-4 4v-4H1z" fill="#fff"/><circle cx="5.5" cy="6" r="1" fill="#4a9a1e"/><circle cx="9" cy="6" r="1" fill="#4a9a1e"/><circle cx="12.5" cy="6" r="1" fill="#4a9a1e"/></svg>
      <div><strong>Got A Question?</strong><span>Get LIVE Support</span></div>
    </div>
  </nav>
</header>

<main>
  <section class="abs notice">
    <svg class="abs" style="left:23px;top:16px" width="38" height="38" viewBox="0 0 38 38"><circle cx="19" cy="19" r="18" fill="#4caf1e" stroke="#cfe8bd" stroke-width="2"/><path d="M10 19l6 6 12-12" stroke="#fff" stroke-width="4.5" fill="none" stroke-linecap="round" stroke-linejoin="round"/></svg>
    <h1>Congratulation!!!</h1>
    <p><a href="#">calmerix.example</a> is available for you.</p>
    <div class="price">Price: <b>$ 8700.00</b></div>
  </section>

  <aside class="abs summary">
    <h2>Order Summary</h2>
    <span class="lbl" style="left:15px;top:45px">Discount Code:</span>
    <div class="field" style="left:112px;top:38px;width:85px"></div>
    <a class="apply" href="#">Apply</a>
    <span class="lbl" style="left:16px;top:78px">Total Amount:</span>
    <div class="total">$ 8700.00</div>
  </aside>

  <h3 class="abs methods">Payment Methods:</h3>
  <div class="tab card">Credit Card</div>
  <div class="tab alt">Coinlane</div>
  <div class="tab invoice">Invoice Me</div>

  <div class="abs band"><span style="left:11px">Enter Billing Details</span><span style="left:561px">Enter Card Info</span></div>

  <form class="abs billing">
    <span class="label" style="left:12px;top:16px">First Name:</span><div class="field" style="left:123px;top:11px;width:133px"></div>
    <span class="label" style="left:286px;top:16px">Last Name:</span><div class="field" style="left:395px;top:11px;width:133px"></div>
    <span class="label" style="left:12px;top:54px">Email:</span><div class="field" style="left:123px;top:49px;width:133px"></div>
    <span class="label" style="left:286px;top:54px">Phone:</span><div class="field" style="left:395px;top:49px;width:133px"></div>
    <span class="label" style="left:12px;top:92px">Organization:</span><div class="field" style="left:123px;top:87px;width:405px"></div>
    <span class="label" style="left:12px;top:130px">Address Line 1:</span><div class="field" style="left:123px;top:125px;width:133px"></div>
    <span class="label" style="left:286px;top:130px">Address Line 2:</span><div class="field" style="left:395px;top:125px;width:133px"></div>
    <span class="label" style="left:12px;top:168px">City/Town:</span><div class="field" style="left:123px;top:163px;width:133px"></div>
    <span class="label" style="left:286px;top:168px">State/Province:</span><div class="select" style="left:395px;top:163px;width:133px">Not Applicable<i></i></div>
    <span class="label" style="left:12px;top:206px">Zip Code:</span><div class="field" style="left:123px;top:201px;width:133px"></div>
    <span class="label" style="left:286px;top:206px">Country:</span><div class="select" style="left:395px;top:201px;width:133px">United States<i></i></div>
  </form>

  <form class="abs cardinfo">
    <span class="label" style="left:30px;top:16px">Card No:</span><div class="field" style="left:140px;top:11px;width:131px"></div>
    <span class="label" style="left:30px;top:54px">Name On Card:</span><div class="field" style="left:140px;top:49px;width:131px"></div>
    <span class="label" style="left:30px;top:92px">Exp. Date:</span>
    <div class="select dark" style="left:140px;top:87px;width:59px">JAN<i></i></div>
    <div class="select dark" style="left:206px;top:87px;width:65px">2013<i></i></div>
    <span class="label" style="left:30px;top:130px">CVV No:</span>
    <svg class="abs" style="left:83px;top:128px" width="17" height="17" viewBox="0 0 17 17"><circle cx="8.5" cy="8.5" r="8.5" fill="#111"/><text x="8.5" y="13" text-anchor="middle" font-family="Arial" font-weight="700" font-size="12" fill="#fff">?</text></svg>
    <div class="field" style="left:140px;top:125px;width:131px"></div>
  </form>
  <p class="abs terms">By completing this transaction, I agree to abide with the <a href="#">Universal Terms.</a></p>
  <div class="abs checkout">
    <svg width="10" height="13" viewBox="0 0 10 13"><path d="M2.5 6V4a2.5 2.5 0 0 1 5 0v2" stroke="#fff" stroke-width="1.8" fill="none"/><rect x="0" y="6" width="10" height="7" rx="1" fill="#fff"/></svg>
    SECURE CHECKOUT
  </div>
</main>

<footer class="abs footer">
  <div class="abs flinks">Home &nbsp;|&nbsp; About &nbsp;|&nbsp; Support &nbsp;|&nbsp; Privacy &nbsp;|&nbsp; Terms &amp; Conditions &nbsp;|&nbsp; Testimonials</div>
  <div class="abs copy">© 2013 Zeprilo.com. All rights reserved.</div>
  <span class="social" style="left:170px"></span>
  <span class="social" style="left:198px"></span>
  <span class="social" style="left:225px"></span>
  <span class="social" style="left:251px"></span>
  <div class="abs badge"><b>100%</b><span>SATISFACTION<br>GUARANTEED</span></div>
  <div class="abs fbrand">ZEPRILO.COM</div>
</footer>
</body>
</html>
```